Electrical panel service sticker w Bucket truck & Logo

We have a rather plain sticker we put on lighting panels to remind customers who to call for service. We want to redesign them with brushed aluminum background. We want a remake of the sticker with the outline of a bucket truck. You'll need to find or draw the outling of a bucket truck maybe with the boom up slightly as we will get these stickers die cut.

We want LOGO with Ph.# and Email.
Electrical * Lighting * Sign Service

Target Market(s)

Commercial property managers

Industry/Entity Type

Property Management

Requirements
Must have
• Bucket Truck Outline

```html
<!DOCTYPE html>
<html lang="en">
<head>
<meta charset="utf-8">
<title>Brightline Facilities – Panel Service Sticker</title>
<link rel="stylesheet" href="https://fonts.googleapis.com/css2?family=Roboto+Condensed:wght@500;700&display=swap">
<style>
  :root {
    --ink: #111111;
    --metal-light: #f4f4f4;
    --metal-mid: #d9d9d9;
    --metal-dark: #bdbdbd;
    --accent-blue: #2f7fc1;
    --art-light: #f7f7f7;
    --art-mid: #9a9a9a;
    --art-dark: #3a3a3a;
  }
  * { margin: 0; padding: 0; box-sizing: border-box; }
  html, body { width: 1200px; height: 900px; overflow: hidden; }
  body { font-family: "Roboto Condensed", "Arial Narrow", sans-serif; color: var(--ink); }

  .sticker {
    position: relative;
    width: 1200px;
    height: 900px;
    background:
      repeating-linear-gradient(180deg, rgba(255,255,255,0.18) 0 1px, rgba(0,0,0,0.025) 1px 3px),
      linear-gradient(90deg, var(--metal-dark) 0%, var(--metal-light) 22%, var(--metal-mid) 45%, var(--metal-light) 62%, var(--metal-light) 75%, var(--metal-dark) 100%);
  }

  .truck-art {
    position: absolute;
    left: 89px;
    top: 214px;
    width: 479px;
    height: 468px;
  }

  .brand-square {
    position: absolute;
    left: 633px;
    top: 292px;
    width: 86px;
    height: 143px;
    background: var(--accent-blue);
  }
  .brand-name {
    position: absolute;
    left: 740px;
    top: 286px;
    font-weight: 700;
    font-size: 72px;
    line-height: 72px;
    letter-spacing: 0.5px;
    text-transform: uppercase;
    white-space: nowrap;
  }
  .brand-name span { display: block; }
  .brand-name span + span { margin-top: 18px; }

  .phone {
    position: absolute;
    left: 633px;
    top: 496px;
    font-weight: 700;
    font-size: 84px;
    line-height: 1;
    white-space: nowrap;
  }
  .email,
  .services {
    position: absolute;
    left: 634px;
    font-weight: 500;
    font-size: 26px;
    line-height: 1;
    letter-spacing: 0.8px;
    text-transform: uppercase;
    white-space: nowrap;
  }
  .email { top: 580px; }
  .services { top: 614px; }
</style>
</head>
<body>
  <main class="sticker">
    <svg class="truck-art" viewBox="0 0 479 468" role="img" aria-label="Black outline illustration of a bucket truck with its boom raised and the bucket lifted">
      <defs>
        <linearGradient id="truck-tone" x1="0" y1="0" x2="0.6" y2="1">
          <stop offset="0" stop-color="var(--art-light)"/>
          <stop offset="0.6" stop-color="var(--art-mid)"/>
          <stop offset="1" stop-color="var(--art-dark)"/>
        </linearGradient>
      </defs>
      <rect x="0" y="0" width="479" height="468" fill="url(#truck-tone)"/>
    </svg>

    <div class="brand-square" aria-hidden="true"></div>
    <h1 class="brand-name">
      <span>Brightline</span>
      <span>Facilities</span>
    </h1>

    <p class="phone">877-555-0148</p>
    <p class="email">service@brightlinefacilities.com</p>
    <p class="services">Electrical • Lighting • Sign Service</p>
  </main>
</body>
</html>
```